GUARANTEED WordPress design needed for a sassy, confident charisma coach!

We need a website design for Marla Penrick's brand new, responsive, Wordpress website.
Marla is a trainer / coach who teaches people how to be more charismatic and runs events, publishes video courses and has an ongoing video blog. Her old website is here: www.marlapenrick.co.uk ... but it's now time to have a much better site!
We have a strong idea about the technical components of the website, but we need a designer's eye to create a great style for the site (and provide layered PSD files which our developers will then convert to HTML and CSS).
Marla's brand is sassy, brave, warm and confident. The videos on her existing site give quite a good feel for her personality. We need a clean, stylish and compelling page that isn't too corporate and captures her personality. Every element needs to feel coherent, from fonts and headings to colours and spacing.
The following sites are not exactly what Marla wants (and certainly aren't right in terms of colours) but they give you an idea of the kind of people she is competing against and the area she is operating in:
http://www.tessa-broughley.example/
http://rowanfelsby.example/
Ideally, you will have done something similar and be able to key in on exactly the kind of thing we want: we're not looking to reinvent the wheel. Hopefully you won't mind tweaking a few things if you are close to what we need.
More detail is provided in the word document attached. But in a nutshell we need: a banner, footer, sign-up strap, menu bar, signature and 4 different basic page types. We want bursts of bright colours, contrasted with black and white if possible - sorry we can't be more specific than that...
The word doc also contains some amateur mock-ups as well (the images are also just mockups at this stage) - but although these give a general sense of the structure what we are looking for, we are clearly not designers...so please help! We need a designer's touch!
Kind regards,
Corin
PS The layered PSD versions of the mockup files are available on Cloudvantre: https://files.cloudvantre.example/sh/k72pqa4w1zbtmrd/QXvenlr8Ty3PwMiU6Hs2kYfDb?dl=0
Target Market(s)
Entrepreneurs who need to sell themselves.
Number of Pages Required
4 page

```html
<!DOCTYPE html>
<html lang="en">
<head>
<meta charset="utf-8">
<title>Marla Penrick – Charisma Coach</title>
<link href="https://fonts.googleapis.com/css2?family=Raleway:wght@400;600;700;800&family=Open+Sans:wght@400;600;700&display=swap" rel="stylesheet">
<style>
:root{
  --purple:#8b2a9c;
  --purple-dark:#6d1f7c;
  --magenta:#b23bc4;
  --lime:#b3d335;
  --yellow:#f3df1c;
  --ink:#222;
  --hero:#262626;
  --grey-bg:#e7e7e7;
  --text:#555;
  --muted:#999;
  --cyan:#22b4e4;
  --orange:#f1a11f;
  --white:#fff;
  --footer:#1c1c1c;
}
*{box-sizing:border-box;margin:0;padding:0}
html,body{width:1200px;height:3308px;overflow:hidden}
body{position:relative;background:var(--grey-bg);font-family:"Open Sans",Arial,sans-serif;color:var(--text)}
.abs{position:absolute}

/* header */
.site-header{left:0;top:0;width:1200px;height:72px;background:var(--white);display:flex;align-items:center;justify-content:space-between;padding:0 40px 0 56px}
.brand{font-family:"Raleway",sans-serif;font-weight:700;font-size:30px;color:var(--purple);display:flex;align-items:center;gap:10px}
.brand-dot{width:12px;height:12px;border-radius:50%;background:var(--purple)}
.main-nav{display:flex;gap:6px}
.main-nav a{font-family:"Raleway",sans-serif;font-weight:600;font-size:13px;color:#444;text-decoration:none;padding:8px 12px;letter-spacing:.5px}
.main-nav a.is-current{border:1px solid #bbb}

/* hero */
.hero{left:0;top:72px;width:1200px;height:568px;background:var(--hero);overflow:hidden}
.hero-photo{position:absolute;left:560px;top:0;width:640px;height:448px;background:radial-gradient(ellipse at 55% 45%,#7a5a4e 0%,#3a302c 45%,#262626 80%)}
.hero-title{position:absolute;left:80px;top:44px;font-family:"Raleway",sans-serif;font-weight:700;font-size:74px;line-height:82px;color:var(--magenta);letter-spacing:1px}
.hero-strip{position:absolute;left:0;top:448px;width:1200px;height:120px;background:var(--lime)}
.hero-laptop{position:absolute;left:24px;top:360px;width:300px;height:190px;border-radius:8px 8px 0 0;background:linear-gradient(135deg,#d8d8d8,#9a9a9a)}
.hero-laptop-screen{position:absolute;left:14px;top:12px;width:272px;height:160px;background:linear-gradient(135deg,#c0392b,#8e44ad)}
.hero-laptop-base{position:absolute;left:0;top:550px;width:348px;height:12px;background:#bfbfbf;border-radius:0 0 10px 10px}
.hero-copy{position:absolute;left:440px;top:462px;width:560px;font-size:17px;line-height:24px;color:var(--ink);font-weight:600}
.hero-copy .accent{color:var(--white)}
.hero-form{position:absolute;left:440px;top:522px;display:flex;gap:10px}
.field{height:30px;width:170px;background:var(--white);border:1px solid #ccc;font-size:11px;color:#999;padding:7px 8px}
.btn{height:30px;padding:6px 16px;background:var(--yellow);color:var(--ink);font-weight:700;font-size:12px}
.hero-note{position:absolute;left:440px;top:560px;font-size:10px;color:#333}

/* posts column */
.post-column{left:88px;top:700px;width:676px;height:2230px;background:var(--white);padding:22px 22px}
.post{margin-bottom:66px}
.post-media{position:relative;height:330px;overflow:hidden}
.post-media .label{position:absolute;left:24px;top:40px;font-family:"Raleway",sans-serif;font-weight:600;font-size:40px;line-height:48px;text-transform:uppercase}
.post-media .sub{position:absolute;left:24px;font-family:"Raleway",sans-serif;font-weight:700;font-size:26px;padding:6px 12px}
.media-dark{background:linear-gradient(120deg,#111 0%,#3b2a26 50%,#7a1f1f 100%)}
.media-grey{background:linear-gradient(90deg,#3a3a3a 0%,#555 55%,#8a7a70 100%)}
.media-cyan{background:linear-gradient(90deg,var(--cyan) 0%,var(--cyan) 60%,#8fd5ee 100%)}
.media-orange{background:linear-gradient(90deg,var(--orange) 0%,var(--orange) 60%,#f6c97a 100%)}
.post-title{margin-top:22px;font-family:"Raleway",sans-serif;font-weight:700;font-size:20px;color:var(--purple);text-transform:uppercase}
.post-excerpt{margin-top:12px;font-size:12px;line-height:19px;color:#777}
.post-excerpt b{color:var(--purple)}
.post-meta{margin-top:12px;display:flex;gap:26px;font-size:10px;color:var(--muted)}
.post-meta span::before{content:"";display:inline-block;width:9px;height:9px;background:#bbb;margin-right:6px;vertical-align:-1px}
.pager{position:absolute;left:0;bottom:56px;width:676px;display:flex;justify-content:center;gap:10px}
.pager span{width:24px;height:24px;border-radius:50%;border:1px solid #aaa;font-size:10px;text-align:center;line-height:22px;color:#888}
.pager span.is-active{background:#888;color:#fff}

/* sidebar */
.widget{left:788px;width:324px;background:var(--white);padding:18px}
.widget-title{font-family:"Raleway",sans-serif;font-weight:700;font-size:15px;color:#444;text-transform:uppercase;padding-bottom:8px;border-bottom:3px solid var(--purple);margin-bottom:14px}
.recent li{list-style:none;font-size:12px;line-height:17px;color:#444;padding:8px 0;border-bottom:1px solid #eee}
.recent small{display:block;font-size:9px;color:var(--muted);margin-top:3px}
.tag-cloud{display:flex;flex-wrap:wrap;gap:5px}
.tag-cloud span{background:var(--purple);color:#fff;padding:3px 7px;font-family:"Raleway",sans-serif}
.video-thumb{height:160px;background:linear-gradient(90deg,#ddd,#888 50%,#ddd)}
.event-card{position:relative;height:520px;background:linear-gradient(160deg,#3b3b3b,#161616 70%);padding:18px;color:#fff}
.event-card .headline{font-family:"Raleway",sans-serif;font-weight:800;font-size:30px;line-height:34px;text-transform:uppercase}
.event-live{position:absolute;left:110px;top:250px;width:180px;height:230px;background:var(--cyan);padding:14px}
.event-live strong{display:block;font-family:"Raleway",sans-serif;font-size:58px;line-height:60px}
.event-live em{display:block;font-style:normal;font-size:20px;line-height:24px;margin:6px 0 12px}
.event-live span{display:inline-block;background:var(--ink);color:#fff;font-weight:700;font-size:15px;padding:8px 14px}
.portrait{left:810px;top:2380px;width:300px;height:690px;background:linear-gradient(180deg,rgba(60,60,60,0) 0%,#dedede 10%,#bdbdbd 60%,#9a9a9a 100%);border-radius:120px 120px 0 0}

/* signup strap */
.signup{left:0;top:3040px;width:1200px;height:148px;background:var(--purple);color:#fff;padding:24px 0 0 88px}
.signup p{width:660px;font-size:17px;line-height:24px;font-weight:600}
.signup-form{display:flex;gap:10px;margin-top:14px}

/* footer */
.site-footer{left:0;top:3188px;width:1200px;height:120px;background:var(--footer);color:#aaa;padding:22px 88px;font-size:11px}
.footer-links{margin-top:10px;display:flex;gap:40px;font-size:9px;letter-spacing:.5px}
.socials{position:absolute;right:92px;top:26px;display:flex;gap:6px}
.socials span{width:30px;height:30px;background:#2a8fd8}
.socials span:nth-child(2){background:#3b5998}
.socials span:nth-child(3){background:#0077b5}
.socials span:nth-child(4){background:#c74a3a}
</style>
</head>
<body>

<header class="site-header abs">
  <div class="brand"><span class="brand-dot"></span>Marla Penrick</div>
  <nav class="main-nav">
    <a class="is-current">HOME</a><a>EVENTS</a><a>WORK WITH ME</a><a>CORPORATE</a><a>ABOUT</a><a>CONTACT</a>
  </nav>
</header>

<section class="hero abs">
  <div class="hero-photo" role="img" aria-label="Portrait photo of Marla smiling"></div>
  <h1 class="hero-title">ATTRACT<br>CONNECT<br>INFLUENCE</h1>
  <div class="hero-strip"></div>
  <div class="hero-laptop"><div class="hero-laptop-screen" role="img" aria-label="Laptop screen showing the free training video"></div></div>
  <div class="hero-laptop-base"></div>
  <p class="hero-copy">Learn how to unlock the superpower* of your charisma and win all the business you want with this <span class="accent">FREE training.</span></p>
  <div class="hero-form"><div class="field">First Name</div><div class="field">Email Address</div><div class="btn">Yes Please</div></div>
  <p class="hero-note">* Promise to only use your power for good!</p>
</section>

<main class="post-column abs">
  <article class="post">
    <div class="post-media media-dark" role="img" aria-label="Photo of a speaker on stage before an audience">
      <span class="label" style="color:#fff">Public<br>speaking...</span>
    </div>
    <h2 class="post-title">Public speaking...made easy</h2>
    <p class="post-excerpt">Walking on stage can feel terrifying, but with a few simple habits you can own the room, calm your nerves and leave every audience wanting more from you. <b>Continue Reading</b></p>
    <div class="post-meta"><span>MAY 10 2016</span><span>2 COMMENTS</span></div>
  </article>
  <article class="post">
    <div class="post-media media-grey" role="img" aria-label="Photo of Marla smiling">
      <span class="label" style="color:#fff">How to start<br>every day in<br>the right<br>frame of mind!</span>
    </div>
    <h2 class="post-title">How to start every day in the right frame of mind!</h2>
    <p class="post-excerpt">Your morning sets the tone for everything that follows. Try these quick rituals to wake up focused, confident and ready to shine in every meeting you walk into. <b>Continue Reading</b></p>
    <div class="post-meta"><span>MAY 03 2016</span><span>4 COMMENTS</span></div>
  </article>
  <article class="post">
    <div class="post-media media-cyan" role="img" aria-label="Photo of Marla with an outfit on a clothes rail">
      <span class="label" style="color:#fff;top:24px">Take charge of your<br>style...</span>
      <span class="sub" style="top:200px;color:#fff;font-size:34px;padding:0">...BOOST YOUR<br>CONFIDENCE</span>
    </div>
    <h2 class="post-title">Take charge of your style...boost your confidence</h2>
    <p class="post-excerpt">What you wear speaks before you do. Discover how a few smart wardrobe choices can lift your posture, sharpen your presence and boost how you feel inside. <b>Continue Reading</b></p>
    <div class="post-meta"><span>APR 26 2016</span><span>3 COMMENTS</span></div>
  </article>
  <article class="post">
    <div class="post-media media-orange" role="img" aria-label="Photo of Marla thinking">
      <span class="label" style="color:#fff;top:24px">Unfulfilled? It's<br>time to think<br>about your<br>values...</span>
      <span class="sub" style="top:240px;background:var(--white);color:var(--orange);font-size:20px">DO THIS EXERCISE NOW!</span>
    </div>
    <h2 class="post-title">Unfulfilled? It's time to think about your values...</h2>
    <p class="post-excerpt">When work feels flat, it is often because you are not living your values. This short exercise will help you name what truly matters and act on it. <b>Continue Reading</b></p>
    <div class="post-meta"><span>APR 19 2016</span><span>5 COMMENTS</span></div>
  </article>
  <div class="pager"><span>&lsaquo;</span><span class="is-active">1</span><span>2</span><span>3</span><span>4</span><span>&rsaquo;</span></div>
</main>

<aside class="widget abs" style="top:700px;height:380px">
  <h3 class="widget-title">Marla says</h3>
  <ul class="recent">
    <li>Be more dog: 3 lessons we could learn from our best friends<small>MAY 17 2016</small></li>
    <li>Are you letting your core beliefs hold you back?<small>MAY 12 2016</small></li>
    <li>How I learned to stop worrying and start NETWORKING<small>MAY 05 2016</small></li>
    <li>Resting face and other strange - but true - problems<small>APR 29 2016</small></li>
  </ul>
</aside>

<aside class="widget abs" style="top:1110px;height:240px">
  <h3 class="widget-title">Tags</h3>
  <div class="tag-cloud">
    <span style="font-size:11px">body language</span>
    <span style="font-size:20px">capsule wardrobe</span>
    <span style="font-size:11px">confidence</span><span style="font-size:11px">handshake</span><span style="font-size:11px">image</span>
    <span style="font-size:12px">make-up</span><span style="font-size:12px">physique</span>
    <span style="font-size:18px">power pose</span>
    <span style="font-size:11px">presentation</span><span style="font-size:11px">presence</span><span style="font-size:11px">public speaking</span>
    <span style="font-size:22px">rapport</span><span style="font-size:11px">spring wear</span><span style="font-size:13px">style</span>
    <span style="font-size:11px">vision board</span><span style="font-size:12px">warmth</span>
  </div>
</aside>

<aside class="widget abs" style="top:1380px;height:250px">
  <h3 class="widget-title">Video</h3>
  <div class="video-thumb" role="img" aria-label="Video still of Marla talking to camera"></div>
</aside>

<aside class="widget abs" style="top:1660px;height:620px">
  <h3 class="widget-title">Coming up!</h3>
  <div class="event-card" role="img" aria-label="Event poster photo of Marla on stage">
    <div class="headline">Unlock<br>the<br>superpower<br>of charisma</div>
    <div class="event-live"><strong>LIVE</strong><em>Only 6<br>places left.</em><span>LEARN<br>MORE</span></div>
  </div>
</aside>

<div class="portrait abs" role="img" aria-label="Full-length photo of Marla in a black and white dress"></div>

<section class="signup abs">
  <p>Hey! Don't go without signing up because you'll miss out on exclusive offers, awesome tips, and weekly motivation in my fab newsletter *.</p>
  <div class="signup-form"><div class="field">First Name</div><div class="field">Email Address</div><div class="btn">Yes Please</div></div>
</section>

<footer class="site-footer abs">
  <div>© 2016 Marla Penrick Ltd</div>
  <div class="footer-links"><span>PRIVACY POLICY</span><span>COOKIE POLICY</span><span>TERMS POLICY</span><span>DISCLAIMER</span></div>
  <div class="socials"><span></span><span></span><span></span><span></span></div>
</footer>

</body>
</html>
```